BRASKET LAND SERVICES BILLBOARD DESIGN

I NEED A BILLBOARD FOR MY BUSINESS. WE ARE A LAND CLEARING COMPANY AND I WOULD LIKE TO ADD A PICTURE OF MY TRACK LOADER TO THE SIGN. OPEN TO COLORS. I WOULD ALSO LIKE TO HAVE MY PHONE NUMBER 555-284-6170, WEBSITE WWW.BRASKETLANDSERVICES.EXAMPLE, AND EMAIL ON THE SIGN (CONTACT@BRASKETLANDSERVICES.EXAMPLE). DESIGNERS CAN HAVE THE FREEDOM TO DO WHATEVER STYLE THEY WANT AND TO USE ANY COLORS THEY WANT.

Target Market(s)

ANYONE WITH PROPERTY

Requirements
Must have
• PICTURE OF TRACK LOADER, WEBSITE, PHONE NUMBER, EMAIL
Nice to have
• OPEN TO ANYTHING
Should not have
• OPEN TO ANYTHING

```html
<!DOCTYPE html>
<html lang="en">
<head>
<meta charset="utf-8">
<title>Brasket Land Services Billboard</title>
<link rel="stylesheet" href="https://fonts.googleapis.com/css2?family=Montserrat:ital,wght@1,800;1,900&display=swap">
<style>
  :root {
    --page: #f2f2f0;
    --board: #1e1e1f;
    --orange: #f28a1e;
    --orange-deep: #ec5f24;
    --white: #ffffff;
    --silver-light: #f1f1f1;
    --silver-mid: #bdbdbd;
    --photo-sky: #e9eadf;
    --photo-trees: #6f8546;
    --photo-grass: #b8a468;
  }
  * { box-sizing: border-box; margin: 0; padding: 0; }
  html, body { width: 974px; height: 1200px; overflow: hidden; background: var(--page); }
  .billboard {
    position: absolute; left: 27px; top: 380px;
    width: 920px; height: 440px;
    background: var(--board);
    overflow: hidden;
    font-family: "Montserrat", sans-serif;
    font-style: italic;
  }
  .billboard-art { position: absolute; inset: 0; width: 100%; height: 100%; }
  .brand-name {
    position: absolute; right: 40px; top: 24px;
    text-align: right;
    font-weight: 900;
    font-size: 62px;
    line-height: 66px;
    letter-spacing: -1px;
    background: linear-gradient(160deg, var(--silver-light) 0%, var(--silver-mid) 45%, var(--silver-light) 70%, var(--silver-mid) 100%);
    -webkit-background-clip: text; background-clip: text;
    color: transparent;
  }
  .call-to-action {
    position: absolute; right: 42px; top: 250px;
    font-weight: 900; font-size: 29px; color: var(--orange);
  }
  .phone {
    position: absolute; right: 40px; top: 284px;
    font-weight: 900; font-size: 47px; color: var(--white); letter-spacing: -0.5px;
  }
  .contact {
    position: absolute; right: 42px; top: 366px;
    text-align: right; font-weight: 800; font-size: 15px; line-height: 21px;
  }
  .contact .website { color: var(--orange); }
  .contact .email { color: var(--white); }
</style>
</head>
<body>
  <section class="billboard">
    <svg class="billboard-art" viewBox="0 0 920 440" preserveAspectRatio="none">
      <defs>
        <linearGradient id="loaderPhotoTone" x1="0" y1="0" x2="0" y2="1">
          <stop offset="0" stop-color="var(--photo-sky)"/>
          <stop offset="0.3" stop-color="var(--photo-trees)"/>
          <stop offset="0.7" stop-color="#7d8a4c"/>
          <stop offset="1" stop-color="var(--photo-grass)"/>
        </linearGradient>
        <linearGradient id="swooshTone" x1="0" y1="0" x2="0" y2="1">
          <stop offset="0" stop-color="var(--orange-deep)"/>
          <stop offset="1" stop-color="var(--orange)"/>
        </linearGradient>
      </defs>
      <path class="loader-photo" role="img" aria-label="Photo of an orange tracked loader with a forestry mulcher attachment on a grassy field in front of trees"
            d="M0,0 H250 C420,60 540,200 528,300 C520,370 450,420 397,440 H0 Z" fill="url(#loaderPhotoTone)"/>
      <path class="swoosh-orange" d="M250,0 H332 C472,70 575,200 562,300 C552,370 505,420 482,440 H397 C450,420 520,370 528,300 C540,200 420,60 250,0 Z" fill="url(#swooshTone)"/>
      <path class="swoosh-white" d="M374,0 H418 C505,60 556,140 572,232 C540,150 470,62 374,0 Z" fill="var(--white)"/>
    </svg>
    <h1 class="brand-name">BRASKET<br>LAND<br>SERVICES</h1>
    <p class="call-to-action">CALL NOW!</p>
    <p class="phone">555-284-6170</p>
    <p class="contact">
      <span class="website">WWW.BRASKETLANDSERVICES.EXAMPLE</span><br>
      <span class="email">CONTACT@BRASKETLANDSERVICES.EXAMPLE</span>
    </p>
  </section>
</body>
</html>
```